Tavo Payments Business card refresh

Need a new design of our business card The info is not what is on these cards i sent this for a reference. I can email all the info over
Info would be Derek Whitfield Chief TAVO is the title. our new address is 47615 Birch Hollow Rd. Westlake Village Ca 91384 Cell number is 805-634-2917 Work number is 855-482-7309 ext 212 Derek@tavopayments.com is my email address
Target Market(s)
Merchant Services all businesses that take credit cards
Industry/Entity Type
Merchant Services / Credit Card processing
Contact Information for Business Card
Need a new design of our business card The info is not what is on these cards i sent this for a reference. I can email all the info over Info would be Derek Whitfield Chief TAVO is the title. our new address is 47615 Birch Hollow Rd. Westlake Village Ca 91384 Cell number is 805-634-2917 Work number is 855-482-7309 ext 212 Derek@tavopayments.com is my email address
Requirements
Must have
- My logo and colors from my brand guidelines
Nice to have
- i sent some designs just need a new refresh
Should not have
- nothing specific

```html
<!DOCTYPE html>
<html lang="en">
<head>
<meta charset="utf-8">
<title>Tavo Payments — Business Card</title>
<link href="https://fonts.googleapis.com/css2?family=Fira+Sans+Condensed:wght@500;600&display=swap" rel="stylesheet">
<style>
  :root {
    --page-bg: #e4e6e1;
    --card-bg: #eef3e7;
    --map-tone: #dfe5d8;
    --ink: #3c4044;
    --green-deep: #45bb2e;
    --green-light: #a8d65e;
    --green-text: #4fb734;
    --white: #ffffff;
  }
  html, body {
    margin: 0;
    padding: 0;
    width: 1200px;
    height: 885px;
    overflow: hidden;
    background: var(--page-bg);
  }
  .card {
    position: absolute;
    left: 75px;
    top: 142px;
    width: 1050px;
    height: 600px;
    background: var(--card-bg);
    overflow: hidden;
    box-shadow: 0 6px 22px rgba(0,0,0,0.18);
    font-family: "Fira Sans Condensed", "Arial Narrow", sans-serif;
  }
  .world-map {
    position: absolute;
    left: 90px;
    top: 20px;
    width: 870px;
    height: 420px;
    border-radius: 40% 45% 35% 40%;
    background: radial-gradient(ellipse at center, var(--map-tone) 0%, rgba(223,229,216,0.6) 55%, rgba(238,243,231,0) 75%);
  }
  .brand {
    position: absolute;
    left: 0;
    width: 100%;
    top: 34px;
    text-align: center;
    font-weight: 600;
    font-size: 46px;
    letter-spacing: 2px;
    color: var(--ink);
    line-height: 1;
  }
  .top-rule {
    position: absolute;
    left: 0;
    top: 106px;
    width: 100%;
    height: 4px;
    background: linear-gradient(90deg, var(--green-deep), var(--green-light));
  }
  .person {
    position: absolute;
    left: 0;
    width: 100%;
    top: 124px;
    margin: 0;
    text-align: center;
    font-weight: 600;
    font-size: 28px;
    line-height: 34px;
    color: var(--ink);
  }
  .person-title {
    color: var(--green-text);
  }
  .services {
    position: absolute;
    left: 0;
    width: 100%;
    top: 178px;
    margin: 0;
    text-align: center;
    font-weight: 500;
    font-size: 27px;
    line-height: 36px;
    color: var(--ink);
  }
  .band {
    position: absolute;
    left: 0;
    top: 384px;
    width: 100%;
    height: 216px;
    background: linear-gradient(90deg, var(--green-deep), var(--green-light));
  }
  .band-edge {
    position: absolute;
    left: 0;
    top: 384px;
    width: 100%;
    height: 10px;
    background: linear-gradient(90deg, #5cc83e, #b4dc72);
  }
  .band-rule {
    position: absolute;
    left: 0;
    top: 400px;
    width: 100%;
    height: 3px;
    background: var(--white);
    opacity: 0.9;
  }
  .tagline {
    position: absolute;
    left: 0;
    width: 100%;
    top: 424px;
    margin: 0;
    text-align: center;
    font-weight: 500;
    font-size: 36px;
    line-height: 44px;
    color: var(--white);
  }
  .contact {
    position: absolute;
    left: 0;
    width: 100%;
    top: 490px;
    margin: 0;
    text-align: center;
    font-weight: 500;
    font-size: 22px;
    line-height: 32px;
    color: var(--white);
  }
  .contact-sep {
    padding: 0 10px;
    opacity: 0.8;
  }
</style>
</head>
<body>
  <div class="card">
    <div class="world-map" role="img" aria-label="Faint world map in the card background"></div>
    <div class="brand">TAVO PAYMENTS</div>
    <div class="top-rule"></div>
    <p class="person">Derek Whitfield <span class="contact-sep">|</span> <span class="person-title">Chief TAVO</span></p>
    <p class="services">
      - Credit Card Processing - White - Glove Support -<br>
      - Same - Day Approval - Merchant Funding -<br>
      - Check Garntee - ACH Deposits -<br>
      - Loyalty Cards - ATM Sales -<br>
      - Gift Cards -
    </p>
    <div class="band"></div>
    <div class="band-edge"></div>
    <div class="band-rule"></div>
    <p class="tagline">Best Rates Best Service - Guaranteed!</p>
    <p class="contact">
      47615 Birch Hollow Rd. Westlake Village, CA 91384<br>
      Cell 805-634-2917<span class="contact-sep">|</span>Work 855-482-7309 ext 212<span class="contact-sep">|</span>Derek@tavopayments.com
    </p>
  </div>
</body>
</html>
```